Norvessa Imports Busisness cards and logo

Norvessa imports is a brand new wholesale company located in Londonderry, New Hampshire dedicated to finding unique products from around the world.
Licensed to sell wine and spirits in the state and also authorized distributors of Velvet Lantern Design, a manufacturer of girls and women shoes. Other products that we are currently trying to import are cheese and frozen food from Spain.
We would like a design that portraits our diversity of products and wholesale capabilities

Reason: Still undecided. Waiting for more feedback from the poll Thanks

```html
<!DOCTYPE html>
<html lang="en">
<head>
<meta charset="utf-8">
<title>Norvessa Imports — Business Cards</title>
<link rel="stylesheet" href="https://fonts.googleapis.com/css2?family=Saira:wght@400;600&display=swap">
<style>
  :root {
    --backdrop: #e6e4df;
    --card-white: #f7f7f5;
    --green-deep: #1f6b22;
    --green-mid: #2f8f2c;
    --green-bright: #3aa236;
    --lime: #9fcf1e;
    --lime-light: #c4e23a;
    --icon-grey: #3d4140;
    --text-light: #ffffff;
    --text-dark: #20301f;
  }
  * { box-sizing: border-box; margin: 0; padding: 0; }
  html, body { width: 1200px; height: 790px; overflow: hidden; }
  body {
    background: var(--backdrop);
    font-family: "Saira", sans-serif;
    display: flex;
    align-items: center;
    justify-content: center;
    gap: 40px;
  }
  .card {
    width: 560px;
    height: 320px;
    position: relative;
    overflow: hidden;
    box-shadow: 0 6px 18px rgba(0,0,0,0.18);
  }

  /* Front */
  .card-front {
    background: var(--card-white);
    display: flex;
    flex-direction: column;
    align-items: center;
    justify-content: center;
    gap: 18px;
  }
  .brand-mark {
    width: 92px; height: 92px;
    border-radius: 50%;
    background: var(--green-bright);
  }
  .brand-name {
    font-weight: 600;
    font-size: 46px;
    color: var(--green-deep);
    line-height: 1;
  }

  /* Back */
  .card-back { background: linear-gradient(135deg, var(--green-mid), var(--green-deep)); }
  .top-edge { position: absolute; top: 0; left: 0; right: 0; height: 10px; background: var(--green-deep); }
  .header-band {
    position: absolute; top: 10px; left: 0; right: 0; height: 84px;
    background: var(--card-white);
    display: flex; align-items: center; justify-content: center; gap: 12px;
  }
  .header-band .brand-mark { width: 50px; height: 50px; }
  .header-band .brand-name { font-size: 28px; }
  .header-rule { position: absolute; top: 94px; left: 0; right: 0; height: 12px; background: var(--green-deep); }

  .contact-list {
    position: absolute; top: 122px; left: 300px; right: 0;
    list-style: none;
    display: flex; flex-direction: column; gap: 7px;
  }
  .contact-item {
    display: flex; align-items: stretch;
    height: 24px;
    background: linear-gradient(90deg, var(--lime), var(--lime-light));
    color: var(--text-dark);
    font-size: 11.5px;
  }
  .contact-item.is-web { background: var(--card-white); }
  .contact-item.is-address { height: 42px; }
  .contact-icon {
    width: 26px; flex: none;
    background: var(--icon-grey);
    display: flex; align-items: center; justify-content: center;
  }
  .contact-icon svg { width: 13px; height: 13px; fill: var(--text-light); }
  .contact-text { padding: 0 10px; display: flex; align-items: center; line-height: 1.2; }

  .person-bar {
    position: absolute; left: 0; bottom: 40px;
    width: 250px; height: 52px;
    display: flex;
  }
  .person-tab { width: 12px; background: var(--icon-grey); }
  .person-info {
    flex: 1;
    background: linear-gradient(90deg, var(--lime), var(--lime-light));
    color: var(--text-light);
    padding: 8px 14px;
    display: flex; flex-direction: column; justify-content: center;
  }
  .person-name { font-size: 15px; letter-spacing: 1px; text-transform: uppercase; line-height: 1.2; }
  .person-role { font-size: 10px; letter-spacing: 0.5px; text-transform: uppercase; }
  .bottom-edge { position: absolute; bottom: 0; left: 0; right: 0; height: 8px; background: var(--green-deep); }
</style>
</head>
<body>
  <section class="card card-front" aria-label="Card front">
    <div class="brand-mark"></div>
    <div class="brand-name">Norvessa Imports</div>
  </section>

  <section class="card card-back" aria-label="Card back">
    <div class="top-edge"></div>
    <header class="header-band">
      <div class="brand-mark"></div>
      <div class="brand-name">Norvessa Imports</div>
    </header>
    <div class="header-rule"></div>

    <ul class="contact-list">
      <li class="contact-item">
        <span class="contact-icon"><svg viewBox="0 0 24 24"><path d="M6.6 10.8a15 15 0 0 0 6.6 6.6l2.2-2.2a1 1 0 0 1 1-.25 11.4 11.4 0 0 0 3.6.57 1 1 0 0 1 1 1V20a1 1 0 0 1-1 1A17 17 0 0 1 3 4a1 1 0 0 1 1-1h3.5a1 1 0 0 1 1 1c0 1.25.2 2.45.57 3.57a1 1 0 0 1-.25 1z"/></svg></span>
        <span class="contact-text">603 555 0148</span>
      </li>
      <li class="contact-item">
        <span class="contact-icon"><svg viewBox="0 0 24 24"><path d="M7 2h10a2 2 0 0 1 2 2v16a2 2 0 0 1-2 2H7a2 2 0 0 1-2-2V4a2 2 0 0 1 2-2zm0 3v13h10V5zm5 14.2a1 1 0 1 0 0 .01z"/></svg></span>
        <span class="contact-text">603 555 0192</span>
      </li>
      <li class="contact-item">
        <span class="contact-icon"><svg viewBox="0 0 24 24"><path d="M3 5h18v14H3zm2 2v.5l7 4.5 7-4.5V7zm0 2.9V17h14V9.9l-7 4.5z"/></svg></span>
        <span class="contact-text">sales@norvessa.com</span>
      </li>
      <li class="contact-item is-web">
        <span class="contact-icon"><svg viewBox="0 0 24 24"><path d="M12 2a10 10 0 1 0 0 20 10 10 0 0 0 0-20zm0 2c.9 1.2 1.6 2.6 2 4h-4c.4-1.4 1.1-2.8 2-4zM4.3 14a8 8 0 0 1 0-4h3.5a16 16 0 0 0 0 4zm.9 2h3c.4 1.5 1 2.9 1.8 4a8 8 0 0 1-4.8-4zm3-8h-3A8 8 0 0 1 10 4c-.8 1.1-1.4 2.5-1.8 4zM12 20c-.9-1.2-1.6-2.6-2-4h4c-.4 1.4-1.1 2.8-2 4zm2.3-6H9.7a14 14 0 0 1 0-4h4.6a14 14 0 0 1 0 4zm.2 6c.8-1.1 1.4-2.5 1.8-4h3a8 8 0 0 1-4.8 4zm1.7-6a16 16 0 0 0 0-4h3.5a8 8 0 0 1 0 4z"/></svg></span>
        <span class="contact-text">www.norvessaimports.com</span>
      </li>
      <li class="contact-item is-address">
        <span class="contact-icon"><svg viewBox="0 0 24 24"><path d="M12 2a7 7 0 0 0-7 7c0 5.2 7 13 7 13s7-7.8 7-13a7 7 0 0 0-7-7zm0 9.5A2.5 2.5 0 1 1 12 6.5a2.5 2.5 0 0 1 0 5z"/></svg></span>
        <span class="contact-text">27 Harbor Mill Road<br>Londonderry NH</span>
      </li>
    </ul>

    <div class="person-bar">
      <div class="person-tab"></div>
      <div class="person-info">
        <span class="person-name">Daniel Rourke</span>
        <span class="person-role">Financial Advisor</span>
      </div>
    </div>
    <div class="bottom-edge"></div>
  </section>
</body>
</html>
```